Medical Professionals- Financial services

We need a logo and stationery designed for a company called Vantor Crest Capital. Based in Queensland Australia, we provide financial services and planning for medical professionals. This includes all aspects of their financial life including Debt, Wealth accumulation, Risk management and ad hoc financial services including legal and accounting.

We do not have any specific requirements for stationery itself, anything that looks quite corporate would be great.

We need stationery for the following
- Business Cards- back
- With compliments
- Letter head
- Email signature
- Display folder

Please note there must be an accredited by KOA logo on all stationery

Must also include "Vantor Crest capital Authorised Representative of Klyde Ostrand Advisory Pty Ltd AFS Licensee no. 518349"

EXCEPTIONS for the business card

Small written, can be anywhere.

Target Market(s)

Medical Professionals- Specialist doctors, Surgeons

Industry/Entity Type

Business

Requirements
Must have
• Must incorporate a medical logo (cross or Caduceus) in a smart way. We would like to see a corporate style logo that will attract to specialist doctors and surgeons.
Nice to have
• Would like to see a corporate style logo

```html
<!DOCTYPE html>
<html lang="en">
<head>
<meta charset="utf-8">
<title>Vantor Crest Capital — Envelope Set</title>
<link rel="stylesheet" href="https://fonts.googleapis.com/css2?family=Montserrat:wght@400;600;700&display=swap">
<style>
  :root {
    --backdrop: #ececec;
    --paper: #f7f7f7;
    --brand-grey: #6d6c70;
    --brand-green: #5cb247;
    --ink-soft: #8a898d;
  }
  html, body {
    margin: 0;
    padding: 0;
    width: 1200px;
    height: 892px;
    overflow: hidden;
    background: var(--backdrop);
    font-family: "Montserrat", sans-serif;
  }
  .canvas {
    position: relative;
    width: 1200px;
    height: 892px;
  }
  .envelope {
    position: absolute;
    width: 760px;
    height: 380px;
    background: var(--paper);
    box-shadow: 0 2px 6px rgba(0,0,0,0.08);
    overflow: hidden;
  }
  .envelope--back { left: 380px; top: 50px; }
  .envelope--front { left: 60px; top: 460px; }

  /* Back */
  .flap {
    position: absolute;
    left: 0; top: 0;
    width: 100%;
    height: 100px;
  }
  .flap__brand {
    position: absolute;
    left: 0; right: 0; top: 40px;
    text-align: center;
    color: #fff;
    font-size: 11px;
    font-weight: 700;
    letter-spacing: 0.12em;
    text-transform: uppercase;
  }
  .licence-note {
    position: absolute;
    left: 0; right: 0; top: 150px;
    text-align: center;
    color: var(--ink-soft);
    font-size: 8px;
    line-height: 1.5;
    margin: 0;
  }

  /* Front */
  .wordmark {
    position: absolute;
    left: 44px; top: 42px;
    display: flex;
    align-items: center;
    gap: 10px;
  }
  .wordmark__square {
    width: 26px; height: 26px;
    background: var(--brand-grey);
  }
  .wordmark__name {
    color: var(--brand-grey);
    font-size: 22px;
    font-weight: 700;
    letter-spacing: 0.02em;
    text-transform: uppercase;
  }
  .return-address {
    position: absolute;
    left: 44px; top: 300px;
    margin: 0;
    color: var(--ink-soft);
    font-size: 9px;
    font-style: normal;
  }
  .base-band {
    position: absolute;
    left: 0; bottom: 0;
    width: 100%;
    height: 30px;
    display: flex;
  }
  .base-band__green { width: 45%; background: var(--brand-green); }
  .base-band__grey { flex: 1; background: var(--brand-grey); }
</style>
</head>
<body>
<main class="canvas">

  <section class="envelope envelope--back" aria-label="Envelope back">
    <svg class="flap" viewBox="0 0 760 100" preserveAspectRatio="none" aria-hidden="true">
      <path d="M0 0 H760 V80 Q760 100 740 100 H0 Z" fill="var(--brand-grey)"/>
    </svg>
    <div class="flap__brand">Vantor Crest Capital</div>
    <p class="licence-note">Vantor Crest capital Authorised Representative<br>of Klyde Ostrand Advisory Pty Ltd AFS Licensee no. 518349</p>
  </section>

  <section class="envelope envelope--front" aria-label="Envelope front">
    <div class="wordmark">
      <span class="wordmark__square"></span>
      <span class="wordmark__name">Vantor Crest Capital</span>
    </div>
    <address class="return-address">418 Harlow Lane, Milton, QLD 4064</address>
    <div class="base-band">
      <span class="base-band__green"></span>
      <span class="base-band__grey"></span>
    </div>
  </section>

</main>
</body>
</html>
```